Vantor Reach Unique Marketing Website Design

I am starting a new company that is a thought leader in the marketing consulting space. The company is called Vantor Reach. We intend to build a Wordpress site on the Astra Theme with the Spectra builder. Our goal is to become the leading voice that empowers high-ticket service business leaders to become Vantor Reach by equipping them with the cutting-edge frameworks and decision grade intelligence taught in leading business schools. What we are looking for is a website design that is clean and professional, making some use of white space well also being eye catching and distinctive in the consulting space. We will probably want to have a video on the homepage not in the hero section, but just below to explain the company and what we do. Our tagline is "Be found. Be chosen." I have attached a brand guide with some messaging, our typography choices, and our color system. The full site will have a primary nav that is four pages - About us, Services, Insights (essentially a blog), and Contact Us. The goal of this project is to develop an art direction that I can give to a designer to build loads of new pages.

Target Market(s)

Business owners (mostly male) from 30-60 years old, looking to fix their sales and marketing funnel.

Industry/Entity Type

Marketing consulting

Font styles to use
Sans Serif

Requirements
Must have
• A clean, professional design that builds trust with owners of high-ticket service businesses. We need a space for explainer video, and sections that tell prospects what we do. Would also like to have a blog carousel.
Nice to have
• Social feeds, if possible. See attached documents for colors and fonts.
Should not have
• Our feel is professional enough to be trustworthy, but unique enough to be memorable. Cartoon ideas do not meet the professional test, and we do not want the website to appear feminine.

```html
<!DOCTYPE html>
<html lang="en">
<head>
<meta charset="utf-8">
<title>Vantor Reach — Be Found. Be Chosen.</title>
<link href="https://fonts.googleapis.com/css2?family=Oswald:wght@500;600;700&family=Lato:wght@400;700;900&display=swap" rel="stylesheet">
<style>
:root{
  --navy:#0c1230;
  --blue:#2a3fe6;
  --blue-bright:#2d48f2;
  --green:#1ea664;
  --mint:#eef9f5;
  --ink:#1b1d2a;
  --body:#3c3f4a;
  --muted:#6b6f7a;
  --gold:#f5b800;
  --white:#ffffff;
}
*{box-sizing:border-box;margin:0;padding:0}
html,body{width:1200px;height:4751px;overflow:hidden}
body{position:relative;background:var(--white);font-family:'Lato',sans-serif;color:var(--body)}
.abs{position:absolute}
.heading{font-family:'Oswald',sans-serif;font-weight:600;color:var(--ink);text-transform:uppercase;letter-spacing:.3px;line-height:1;font-size:44px}
.rule{position:absolute;height:3px;width:56px;background:var(--blue)}
.btn{position:absolute;display:flex;align-items:center;justify-content:center;background:var(--green);color:var(--white);font-family:'Lato',sans-serif;font-weight:700;font-size:15px;border-radius:3px}
.photo{position:absolute}

/* hero */
.hero-bg{position:absolute;left:0;top:0}
.brand{position:absolute;display:flex;align-items:center;gap:10px;font-family:'Lato',sans-serif;font-weight:700;color:var(--white);line-height:1}
.brand .mark{display:block;background:var(--green)}
.nav a{position:absolute;color:var(--white);font-size:14px;text-decoration:none;top:56px}
.nav .active{background:var(--blue-bright);border-radius:3px;padding:6px 10px;top:49px}
.hero-title{font-family:'Oswald',sans-serif;font-weight:700;color:var(--blue-bright);font-size:58px;letter-spacing:.5px;line-height:1}
.hero-sub{color:var(--white);font-size:27px;line-height:1.2}
.hero-copy{color:#e6e8f2;font-size:20px;line-height:31px;width:480px}
.dot{position:absolute;width:10px;height:10px;border-radius:50%;border:1.5px solid #c5c9dd;top:662px}

/* services */
.arrow{position:absolute;width:32px;height:32px;border-radius:50%;background:var(--green)}
.service-card{position:absolute;width:308px}
.service-card .photo{left:0;top:0;width:308px;height:188px}
.service-icon{position:absolute;left:0;top:216px;width:42px;height:42px;border-radius:3px}
.service-title{position:absolute;left:64px;top:224px;font-family:'Oswald',sans-serif;font-weight:600;font-size:22px;line-height:28px;color:var(--ink)}
.service-text{position:absolute;left:0;top:288px;font-size:15px;line-height:22px;width:300px;color:var(--body)}
.service-line{position:absolute;top:372px;height:2px}

/* about */
.para{font-size:14.5px;line-height:26px;color:var(--body);text-align:justify}

/* why */
.why-card{position:absolute;top:2787px;width:308px;height:223px;background:var(--white);box-shadow:0 3px 14px rgba(20,30,60,.12);text-align:center}
.why-card h3{font-family:'Oswald',sans-serif;font-weight:600;font-size:22px;line-height:28px;color:var(--ink);margin-top:92px}
.why-card p{font-size:14px;line-height:22px;color:var(--muted);margin:8px 28px 0}
.why-card svg{position:absolute;left:124px;top:20px}
.why-card.featured{background:var(--blue-bright)}
.why-card.featured h3,.why-card.featured p{color:var(--white)}

/* testimonials */
.quote-card{position:absolute;top:3861px;width:310px;height:230px;background:var(--white);box-shadow:0 3px 14px rgba(20,30,60,.12)}
.quote-mark{position:absolute;left:30px;top:10px;font-family:Georgia,serif;font-size:64px;color:#d8dbe2;line-height:1}
.stars{position:absolute;right:30px;top:30px;color:var(--gold);font-size:17px;letter-spacing:1px}
.quote-text{position:absolute;left:32px;top:78px;width:250px;font-size:15.5px;line-height:26px;color:var(--body)}
.quote-date{position:absolute;left:32px;top:192px;font-size:15.5px;color:var(--body)}

/* footer */
.foot-title{font-family:'Oswald',sans-serif;font-weight:500;font-size:20px;line-height:1.2;color:var(--white)}
.foot-link{font-size:15px;line-height:1.3;color:#e6e8f2}
.social{position:absolute;top:4599px;width:28px;height:28px;border:2px solid var(--white);border-radius:50%}
</style>
</head>
<body>

<!-- HERO -->
<svg class="hero-bg" width="1200" height="820" viewBox="0 0 1200 820">
  <defs>
    <radialGradient id="heroGlow" cx="0.78" cy="0.38" r="0.55">
      <stop offset="0" stop-color="#3a4f8f"/>
      <stop offset="0.5" stop-color="#17204a"/>
      <stop offset="1" stop-color="#0c1230"/>
    </radialGradient>
  </defs>
  <path d="M0 0H1200V627Q600 811 0 627Z" fill="url(#heroGlow)"/>
  <path d="M110 655Q600 815 1090 655" fill="none" stroke="var(--green)" stroke-width="7" stroke-linecap="round"/>
</svg>
<div class="photo" role="img" aria-label="Hand holding a compass over a glowing network of data hexagons" style="left:640px;top:0;width:560px;height:600px;background:radial-gradient(ellipse at 60% 45%,rgba(120,140,190,.35),rgba(12,18,48,0) 70%)"></div>

<div class="brand" style="left:110px;top:54px;font-size:26px"><span class="mark" style="width:16px;height:16px"></span>Vantor Reach</div>
<nav class="nav">
  <a class="active" style="left:526px">Home</a>
  <a style="left:620px">About Us</a>
  <a style="left:728px">Services</a>
  <a style="left:832px">Insights</a>
</nav>
<div class="btn" style="left:952px;top:44px;width:136px;height:40px;font-size:14px">Contact Us</div>

<div class="abs hero-title" style="left:108px;top:203px">BE FOUND. BE CHOSEN.</div>
<div class="abs hero-sub" style="left:108px;top:286px">Where demand becomes a discipline.</div>
<div class="abs hero-copy" style="left:112px;top:339px">We equip high-ticket service firms with the same demand frameworks taught in the world’s leading business schools.</div>
<div class="btn" style="left:112px;top:472px;width:190px;height:42px">See How It Works</div>

<div class="dot" style="left:572px;background:var(--blue-bright);border-color:var(--blue-bright)"></div>
<div class="dot" style="left:590px"></div>
<div class="dot" style="left:605px"></div>
<div class="dot" style="left:620px"></div>

<!-- SERVICES -->
<div class="abs heading" style="left:0;width:1200px;text-align:center;top:822px">Our Services</div>
<div class="rule" style="left:572px;top:875px"></div>

<div class="arrow" style="left:58px;top:1001px"><svg width="32" height="32"><path d="M19 10l-6 6 6 6" fill="none" stroke="#fff" stroke-width="3"/></svg></div>
<div class="arrow" style="left:1108px;top:1001px"><svg width="32" height="32"><path d="M13 10l6 6-6 6" fill="none" stroke="#fff" stroke-width="3"/></svg></div>

<div class="service-card" style="left:110px;top:918px">
  <div class="photo" role="img" aria-label="Team of colleagues discussing work around a tablet in a bright office" style="background:linear-gradient(135deg,#c9ccd2,#6f7480 60%,#3d3f48)"></div>
  <div class="service-icon" style="background:var(--blue-bright)"><svg width="42" height="42"><circle cx="21" cy="21" r="11" fill="none" stroke="#fff" stroke-width="2"/><circle cx="21" cy="21" r="5" fill="none" stroke="#fff" stroke-width="2"/><path d="M21 21L31 11" stroke="#fff" stroke-width="2"/></svg></div>
  <div class="service-title">Demand Strategy</div>
  <div class="service-text">Excepteur sint occaecat cupidatat non proident, sunt in culpa qui officia deser unt mollit anim id est laborum.</div>
  <div class="service-line" style="left:4px;width:302px;background:var(--blue-bright)"></div>
</div>
<div class="service-card" style="left:445px;top:918px">
  <div class="photo" role="img" aria-label="Presenter in front of a screen showing a red bar chart to an audience" style="background:linear-gradient(135deg,#3b4250,#8a94a4 50%,#2c313b)"></div>
  <div class="service-icon" style="background:var(--green)"><svg width="42" height="42"><rect x="10" y="11" width="22" height="16" fill="none" stroke="#fff" stroke-width="2"/><path d="M15 23v-5M20 23v-8M25 23v-3M21 27v5M15 32h12" stroke="#fff" stroke-width="2"/></svg></div>
  <div class="service-title">Executive Enablement</div>
  <div class="service-text">Excepteur sint occaecat cupidatat non proident, sunt in culpa qui officia deseru mollit anim id est laborum.</div>
  <div class="service-line" style="left:4px;width:150px;background:var(--green)"></div>
</div>
<div class="service-card" style="left:780px;top:918px">
  <div class="photo" role="img" aria-label="Person working on a tablet with charts beside a laptop keyboard" style="background:linear-gradient(135deg,#6b4a3c,#b9b2aa 50%,#e2ded8)"></div>
  <div class="service-icon" style="background:var(--green)"><svg width="42" height="42"><rect x="10" y="10" width="22" height="22" fill="none" stroke="#fff" stroke-width="2"/><path d="M14 26l5-6 4 3 6-8" fill="none" stroke="#fff" stroke-width="2"/></svg></div>
  <div class="service-title">Go-to-market Systems</div>
  <div class="service-text">Excepteur sint occaecat cupidatat non proident, sunt in culpa qui officia deseru mollit anim id est laborum.</div>
  <div class="service-line" style="left:4px;width:150px;background:var(--green)"></div>
</div>

<!-- ABOUT -->
<svg class="abs" style="left:100px;top:1398px" width="460" height="450">
  <path d="M330 44A216 216 0 0 1 230 448" fill="none" stroke="var(--blue-bright)" stroke-width="5"/>
</svg>
<div class="photo" role="img" aria-label="Business meeting with a man explaining an idea to colleagues at a table" style="left:112px;top:1406px;width:432px;height:432px;border-radius:50%;background:linear-gradient(135deg,#d8dbe0,#8c8f96 50%,#3c3a3c)"></div>

<div class="abs heading" style="left:641px;top:1417px">About Us</div>
<div class="rule" style="left:643px;top:1469px"></div>
<div class="abs para" style="left:642px;top:1513px;width:445px">Vantor Reach exists to help high-ticket service firms win in markets where trust, expertise, and relevance determine choice. We work with founders and leadership teams who know that growth doesn’t come from more tactics—it comes from clearer thinking.</div>
<div class="abs para" style="left:642px;top:1642px;width:445px">Our work is grounded in the same demand frameworks and decision models taught in leading business schools, adapted for real-world service businesses.</div>
<div class="btn" style="left:643px;top:1768px;width:146px;height:42px">Read More</div>

<!-- VIDEO BAND -->
<svg class="abs" style="left:0;top:1900px" width="1200" height="700">
  <defs>
    <linearGradient id="bandTint" x1="0" y1="0" x2="0" y2="1">
      <stop offset="0" stop-color="#2d44e6"/>
      <stop offset="0.55" stop-color="#3a4fd8"/>
      <stop offset="1" stop-color="#4b5370"/>
    </linearGradient>
  </defs>
  <path d="M110 110Q600 -40 1090 110" fill="none" stroke="var(--green)" stroke-width="7" stroke-linecap="round"/>
  <path d="M0 130Q600 70 1200 130V693H0Z" fill="url(#bandTint)"/>
</svg>
<div class="photo" role="img" aria-label="Four business professionals meeting around a table, tinted blue" style="left:0;top:2180px;width:1200px;height:413px;background:linear-gradient(180deg,rgba(60,78,220,0),rgba(40,44,60,.35))"></div>
<div class="abs heading" style="left:0;width:1200px;text-align:center;top:2047px;font-size:46px;color:var(--white)">Become a Vantor Reach Pro</div>
<div class="rule" style="left:572px;top:2097px;background:var(--white)"></div>
<div class="abs" style="left:300px;width:600px;text-align:center;top:2124px;font-size:19px;line-height:30px;color:var(--white)">A two-minute introduction to the frameworks we use to help service leaders win in competitive markets.</div>
<div class="btn" style="left:515px;top:2212px;width:170px;height:42px">Watch the Video</div>

<!-- WHY CHOOSE US -->
<svg class="abs" style="left:0;top:2593px" width="1200" height="580">
  <path d="M0 0H1200V455Q600 620 0 455Z" fill="var(--mint)"/>
  <path d="M110 487Q600 643 1090 487" fill="none" stroke="var(--blue-bright)" stroke-width="7" stroke-linecap="round"/>
</svg>
<div class="abs heading" style="left:0;width:1200px;text-align:center;top:2680px">Why Choose Us</div>
<div class="rule" style="left:572px;top:2733px"></div>

<div class="arrow" style="left:58px;top:2842px"><svg width="32" height="32"><path d="M19 10l-6 6 6 6" fill="none" stroke="#fff" stroke-width="3"/></svg></div>
<div class="arrow" style="left:1108px;top:2842px"><svg width="32" height="32"><path d="M13 10l6 6-6 6" fill="none" stroke="#fff" stroke-width="3"/></svg></div>

<div class="why-card" style="left:110px">
  <svg width="60" height="60" fill="none" stroke="var(--green)" stroke-width="2.5"><rect x="22" y="22" width="16" height="16"/><path d="M30 6v16M30 38v16M6 30h16M38 30h16M13 13l9 9M47 13l-9 9M13 47l9-9M47 47l-9-9"/><circle cx="30" cy="5" r="3"/><circle cx="30" cy="55" r="3"/><circle cx="5" cy="30" r="3"/><circle cx="55" cy="30" r="3"/></svg>
  <h3>Built on<br>Proven Frameworks</h3>
  <p>Our work is grounded in demand and strategy frameworks taught in ..</p>
</div>
<div class="why-card featured" style="left:445px">
  <svg width="60" height="60" fill="none" stroke="#fff" stroke-width="2.5"><circle cx="26" cy="32" r="16"/><circle cx="26" cy="32" r="7"/><path d="M22 38l4 4 8-9"/><rect x="40" y="6" width="14" height="18"/><path d="M44 12h6M44 17h6"/></svg>
  <h3>Built for<br>High-Ticket Services</h3>
  <p>Everything we do is built for firms where expertise, trust, and ..</p>
</div>
<div class="why-card" style="left:780px">
  <svg width="60" height="60" fill="none" stroke="var(--green)" stroke-width="2.5"><circle cx="30" cy="32" r="7"/><path d="M18 54c0-9 5-14 12-14s12 5 12 14"/><circle cx="12" cy="30" r="5"/><circle cx="48" cy="30" r="5"/><path d="M30 6v16M22 12l8-6 8 6M4 50c0-6 3-10 8-10M56 50c0-6-3-10-8-10"/></svg>
  <h3>Decision-<br>Grade Intelligence</h3>
  <p>We deliver insight leaders can trust and act on, not dashboards or ..</p>
</div>

<!-- READY -->
<div class="abs heading" style="left:110px;top:3255px">Ready to Be Chosen?</div>
<div class="rule" style="left:112px;top:3308px"></div>
<div class="abs para" style="left:110px;top:3351px;width:438px">Vantor Reach works with high-ticket service leaders to bring clarity and discipline to demand strategy. By applying proven frameworks and decision-grade intelligence, we help firms build relevance, earn trust, and create sustainable demand in competitive markets.</div>
<div class="abs para" style="left:110px;top:3505px;width:438px">Let’s explore how disciplined demand strategy and decision-grade intelligence can support your next phase of growth.</div>
<div class="btn" style="left:112px;top:3598px;width:214px;height:42px">Start the Conversation</div>

<svg class="abs" style="left:640px;top:3220px" width="460" height="450">
  <path d="M58 120A216 216 0 0 0 300 444" fill="none" stroke="var(--green)" stroke-width="5"/>
</svg>
<div class="photo" role="img" aria-label="Hands pointing at a tablet showing analytics charts during a meeting" style="left:654px;top:3226px;width:432px;height:432px;border-radius:50%;background:linear-gradient(135deg,#5a4a44,#b7b3b2 45%,#3d3f48)"></div>

<!-- TESTIMONIALS -->
<div class="abs heading" style="left:0;width:1200px;text-align:center;top:3764px">What Our Customers Say</div>
<div class="rule" style="left:572px;top:3815px"></div>

<div class="quote-card" style="left:110px">
  <div class="quote-mark">“</div><div class="stars">★★★★★</div>
  <div class="quote-text">Lorem ipsum dolor sit amet, conse ur adipiscing elit, sed do eiusmod tempo incididunt ut labore et dolore magna aliqua.</div>
  <div class="quote-date">27/01/2026</div>
</div>
<div class="quote-card" style="left:443px">
  <div class="quote-mark">“</div><div class="stars">★★★★★</div>
  <div class="quote-text">Lorem ipsum dolor sit amet, conse ur adipiscing elit, sed do eiusmod tempo incididunt ut labore et dolore magna aliqua.</div>
  <div class="quote-date">4 days ago</div>
</div>
<div class="quote-card" style="left:776px">
  <div class="quote-mark">“</div><div class="stars">★★★★★</div>
  <div class="quote-text">Lorem ipsum dolor sit amet, conse ur adipiscing elit, sed do eiusmod tempo incididunt ut labore et dolore magna aliqua.</div>
  <div class="quote-date">27/01/2026</div>
</div>

<!-- FOOTER -->
<svg class="abs" style="left:0;top:4180px" width="1200" height="571">
  <path d="M110 100Q600 -60 1090 100" fill="none" stroke="var(--blue-bright)" stroke-width="7" stroke-linecap="round"/>
  <path d="M0 133Q600 -10 1200 133V571H0Z" fill="var(--navy)"/>
</svg>
<div class="brand" style="left:0;width:1200px;justify-content:center;top:4322px;font-size:44px"><span class="mark" style="width:24px;height:24px"></span>Vantor Reach</div>

<div class="abs foot-title" style="left:110px;top:4452px">About Us</div>
<div class="abs foot-link" style="left:110px;top:4510px;width:290px;line-height:25px">Lorem ipsum dolor sit amet, conseur adipiscing elit, sed do eiusmod tempo incididunt ut labore magna aliqua.</div>
<div class="social" style="left:114px;background:var(--green);border-color:var(--green)" role="img" aria-label="Social profile"></div>
<div class="social" style="left:164px" role="img" aria-label="Social profile"></div>
<div class="social" style="left:212px" role="img" aria-label="Social profile"></div>
<div class="social" style="left:260px" role="img" aria-label="Social profile"></div>

<div class="abs foot-title" style="left:465px;top:4436px">Main Links</div>
<div class="abs foot-link" style="left:465px;top:4484px">Home</div>
<div class="abs foot-link" style="left:465px;top:4522px">About Us</div>
<div class="abs foot-link" style="left:465px;top:4560px">Services</div>
<div class="abs foot-link" style="left:465px;top:4599px">Contact Us</div>

<div class="abs foot-title" style="left:667px;top:4436px">Contact Us</div>
<svg class="abs" style="left:667px;top:4486px" width="20" height="22" fill="none" stroke="#e6e8f2" stroke-width="1.6"><path d="M10 20s7-7 7-12A7 7 0 0 0 3 8c0 5 7 12 7 12z"/><circle cx="10" cy="8" r="2.5"/></svg>
<div class="abs foot-link" style="left:706px;top:4484px;line-height:25px;width:200px">48 Harbor Lane, Suite 5 Westfield 20417</div>
<svg class="abs" style="left:667px;top:4554px" width="20" height="20" fill="none" stroke="#e6e8f2" stroke-width="1.6"><path d="M4 2h4l2 5-3 2a11 11 0 0 0 4 4l2-3 5 2v4a2 2 0 0 1-2 2A16 16 0 0 1 2 4a2 2 0 0 1 2-2z"/></svg>
<div class="abs foot-link" style="left:706px;top:4554px">+ 1 555 010 4820</div>
<svg class="abs" style="left:667px;top:4600px" width="20" height="16" fill="none" stroke="#e6e8f2" stroke-width="1.6"><rect x="1" y="1" width="18" height="14"/><path d="M1 2l9 7 9-7"/></svg>
<div class="abs foot-link" style="left:706px;top:4599px">hello@vantorreach.com</div>

<div class="abs foot-title" style="left:955px;top:4436px">Other Links</div>
<div class="abs foot-link" style="left:955px;top:4484px">Insights</div>
<div class="abs foot-link" style="left:955px;top:4522px">Cookies Policy</div>
<div class="abs foot-link" style="left:955px;top:4560px">Terms &amp; Conditions</div>
<div class="abs foot-link" style="left:955px;top:4599px">Privacy Policy</div>

<div class="abs" style="left:0;width:1200px;text-align:center;top:4716px;font-size:13px;color:#d9dbe6">Copyright © 2026 Vantor Reach. All rights reserved.</div>

</body>
</html>
```